Don Lucero brick

Product: Vegetable Whipping Cream
Packaging: Brick Cubra Fold (160 mm x 94 mm x 62 mm)
Consumers: bakeries and pastry professionals, artisans
Direction: craftsmanship
Elements that must appear on the packaging:
Logo: see attachment
Items: icons for product uses:
whipping
filling
gas whipping
Features of the product:
100% vegetal fats
the best yeld in volume
high stability
Quantity: e 1L

Left side of the brick:
Ingredients: water, partially hydrogenated palm oil, sugar, stabilizers (E420, E460, E466), emulsifiers (E472b, E 322 (soy lecithin), E471), milk protein, salt, flavor, acidity regulators (E340, E331), coloring (E160a)
Nutrition information per 100g:
Energy Value 290 kcal / 1210 kJ,
28g Fat 26g of which saturates,
Carbohydrate 11g of which sugars 9.5g
Protein 0.6g,
Salt 0.05g
Storage conditions:
Store at temperatures between + 2C and + 18C. Do not freeze.
Best before: see date on the packaging.
Directions to use:
To get the ideal output we recommand to keep the product in the refrigerator before using for 24 hours (at mixing it is recommended for the product to have a maximum temperature of 8C). Professional product can be prepared manually or using any type of mixer or food processor. We recommend a medium mixing speed in the first phase to avoid scattering losses, after which you can mix at high speed until you get the desired consistency. It is recommended not to mix more than necessary. Refrigerate mixed product.
Valtrum Logo: see the attachment
Production place: UE
High Light: Professionals choices

The second face is the same layout and the same information in romanian language
Product: „Cremă vegetală pentru cofetării”
text: se bate – icon image - whipping
text: pentru ganaj – icon image - filling
text: utilizare cu sifon – icon image – gas whipping

Features of the product:
text: 100% grasimi vegetale – icon image - 100% vegetal fats
text: randament ridicat – icon image - the best yeld in volume
text: stabilitate ridicată – icon image - high stability
Quantity: e 1L
Right side of the brick:
Ingrediente: apã, ulei de palmier parţial hidrogenat, zahăr, stabilizatori (E420, E460, E466), emulgatori (E472b, E 322 (lecitinã din soia), E471), proteine din lapte, sare, aromã, corectori de aciditate (E340,E331), colorant (E160a).

Valori nutriţionale pentru 100g :
Valoare energeticã 290 kcal/1210 kJ,
Lipide 28g din care acizi graşi saturaţi 26g,
Glucide 11g din care zaharuri 9.5g
Proteine 0.6g,
Sare 0.05g
Condiții de păstrare:
Se păstrează la temperaturi între +2C şi +18C. A nu se congela .
A se consuma înainte de: vezi data pe ambalaj.
Mod de utilizare:
Pentru a obţine produsul profesional ideal se recomandă ţinerea produsului la frigider, înainte de preparare cu 24 ore (este recomandat ca produsul să aibă o temperatură de maxim 8Cͦ la mixare). Produsul profesional se poate pregăti manual sau cu ajutorul oricărui tip de mixer sau robot de bucătărie. Se recomandă o viteză de mixare medie în prima fază, pentru a evita pierderile prin imprăştiere, după care se poate mixa la viteza mare pană la obţinerea consistenţei dorite. Se recomandă să nu se mixeze mai mult decât este necesar. Refrigeraţi produsul mixat.
Produs in UE

High Light: „Alegerea Profesioniștilor” or: „Creat de artizani pentru artizani”? or „Alegerea maeștrilor artizani”

Reason: Dear Sir, We want to extend the deadline with 10 days for our project "Don Lucero Brick". It is possible to do that? Can you help us to reach more designs? Best regards, Teodor

```html
<!DOCTYPE html>
<html lang="en">
<head>
<meta charset="utf-8">
<title>Don Lucero Brick – Vegetable Whipping Cream</title>
<link rel="stylesheet" href="https://fonts.googleapis.com/css2?family=Oswald:wght@400;600;700&family=Roboto+Condensed:wght@400;700&display=swap">
<style>
  :root {
    --stage: #ececec;
    --paper: #ffffff;
    --panel: #fafafa;
    --green: #79b443;
    --green-deep: #5e9a2e;
    --green-soft: #e4efd3;
    --orange: #ef7d3a;
    --orange-deep: #e0662a;
    --yellow: #f8d57a;
    --yellow-soft: #fbe7b3;
    --ink: #5a5a5a;
    --ink-soft: #8a8a8a;
    --maker: #3c7ab8;
    --white: #ffffff;
  }
  * { box-sizing: border-box; margin: 0; padding: 0; }
  html, body { width: 1200px; height: 995px; overflow: hidden; }
  body { background: var(--stage); font-family: "Oswald", sans-serif; position: relative; }
  .icon-defs { position: absolute; width: 0; height: 0; }

  .dieline {
    position: absolute; left: 58px; top: 208px;
    display: flex; gap: 24px; align-items: flex-start;
  }
  .carton { display: flex; box-shadow: 0 10px 30px rgba(0,0,0,.12); }

  /* front face */
  .face { width: 320px; height: 578px; background: var(--paper); position: relative; overflow: hidden; }
  .face--ro { --accent: var(--green); --accent-deep: var(--green-deep); --band: var(--green-soft); --soft-from: var(--green-soft); --soft-to: var(--green); }
  .face--en { --accent: var(--orange); --accent-deep: var(--orange-deep); --band: var(--yellow); --soft-from: var(--yellow); --soft-to: var(--orange); }

  .ornament {
    position: absolute; left: 18px; top: 14px; width: 284px; height: 150px; border-radius: 10px;
    background: radial-gradient(ellipse at center, transparent 38%, color-mix(in srgb, var(--accent) 22%, transparent) 70%);
  }
  .brand { position: absolute; left: 0; right: 0; top: 58px; display: flex; justify-content: center; align-items: center; gap: 8px; }
  .brand__dot { width: 14px; height: 14px; border-radius: 50%; background: var(--accent); }
  .brand__name { font-weight: 700; font-size: 28px; letter-spacing: .5px; color: var(--accent); text-transform: uppercase; }
  .range {
    position: absolute; left: 95px; right: 95px; top: 112px;
    background: var(--band); color: var(--accent-deep);
    font-size: 11px; letter-spacing: 1.5px; text-align: center; padding: 2px 0; text-transform: uppercase;
  }

  .hero { position: absolute; left: 0; right: 0; top: 172px; height: 178px; background: var(--accent); }
  .hero__title { position: absolute; left: 16px; top: 14px; color: var(--white); font-weight: 700; text-transform: uppercase; line-height: .98; z-index: 1; }
  .face--ro .hero__title { font-size: 38px; }
  .face--ro .hero__title small { display: block; font-size: 16px; font-weight: 600; margin-top: 4px; letter-spacing: .5px; }
  .face--en .hero__title { font-size: 32px; }
  .hero__band { position: absolute; left: 0; top: 106px; width: 196px; height: 56px; background: var(--yellow); }
  .hero__band span { position: absolute; left: 16px; top: 0; font-size: 50px; font-weight: 700; line-height: 56px; color: var(--orange); text-transform: uppercase; }
  .hero__swirl {
    position: absolute; right: 14px; top: -16px; width: 100px; height: 128px;
    border-radius: 50% 50% 40% 40%;
    background: radial-gradient(circle at 40% 35%, #ffffff 55%, #eeeeee 100%);
  }
  .qty {
    position: absolute; width: 54px; height: 54px; border-radius: 50%;
    background: var(--yellow-soft); border: 2px solid var(--yellow); color: var(--ink);
    text-align: center; display: flex; flex-direction: column; justify-content: center; z-index: 2;
  }
  .face--ro .qty { left: 176px; top: 290px; }
  .face--en .qty { left: 212px; top: 282px; }
  .qty__label { font-size: 6.5px; letter-spacing: .5px; text-transform: uppercase; }
  .qty__value { font-size: 16px; font-weight: 700; line-height: 1; }

  .uses {
    position: absolute; left: 16px; right: 16px; top: 372px; list-style: none;
    display: grid; grid-template-columns: repeat(3, 1fr); column-gap: 12px; row-gap: 12px;
  }
  .use { text-align: center; }
  .use__icon {
    height: 66px; border-radius: 2px;
    background: linear-gradient(160deg, var(--accent) 0%, var(--accent-deep) 100%);
    display: flex; align-items: center; justify-content: center;
  }
  .use:nth-child(n+4) .use__icon { background: linear-gradient(160deg, var(--soft-from) 0%, var(--soft-to) 100%); }
  .use__icon svg { width: 40px; height: 40px; }
  .use__label {
    margin-top: 5px; font-size: 8px; line-height: 1.15; letter-spacing: .3px;
    color: var(--ink); text-transform: uppercase; min-height: 18px;
  }

  /* side panel */
  .side {
    width: 210px; height: 578px; background: var(--panel); border-left: 1px solid #e2e2e2;
    padding: 20px 14px 14px; font-family: "Roboto Condensed", sans-serif;
    color: var(--ink); font-size: 7.2px; line-height: 1.3; position: relative;
  }
  .side--ro { --head: var(--green-deep); }
  .side--en { --head: var(--orange); }
  .side__block { margin-bottom: 8px; }
  .side__heading {
    font-family: "Oswald", sans-serif; font-weight: 600; font-size: 8.5px; color: var(--head);
    text-transform: uppercase; letter-spacing: .5px; margin-bottom: 2px;
  }
  .nutrition { width: 100%; border-collapse: collapse; }
  .nutrition td { padding: 1px 0; border-bottom: 1px solid #e6e6e6; }
  .nutrition td:last-child { text-align: right; white-space: nowrap; }
  .side__highlight { margin-top: 6px; font-family: "Oswald", sans-serif; font-size: 11px; font-weight: 600; color: var(--head); text-transform: uppercase; }
  .maker { position: absolute; left: 14px; bottom: 16px; display: flex; align-items: center; gap: 5px; }
  .maker__square { width: 9px; height: 9px; background: var(--maker); }
  .maker__name { font-weight: 700; font-size: 10px; color: var(--maker); text-transform: uppercase; }
  .origin { position: absolute; right: 14px; bottom: 17px; font-size: 7.5px; color: var(--ink-soft); }
</style>
</head>
<body>
<svg class="icon-defs" aria-hidden="true">
  <defs>
    <symbol id="i-whip" viewBox="0 0 40 40"><g fill="none" stroke="#fff" stroke-width="2.2" stroke-linecap="round"><path d="M6 20h28a14 12 0 0 1-28 0z"/><path d="M26 20L34 4"/><path d="M12 18c2-4 6-5 9-3"/></g></symbol>
    <symbol id="i-fill" viewBox="0 0 40 40"><g fill="none" stroke="#fff" stroke-width="2.2" stroke-linejoin="round"><rect x="6" y="24" width="28" height="9" rx="1"/><rect x="8" y="15" width="24" height="9" rx="1"/><path d="M11 15c2-6 16-6 18 0"/></g></symbol>
    <symbol id="i-siphon" viewBox="0 0 40 40"><g fill="none" stroke="#fff" stroke-width="2.2" stroke-linejoin="round"><rect x="13" y="13" width="14" height="22" rx="3"/><rect x="15" y="7" width="10" height="6" rx="1"/><path d="M25 9h7l-2 5"/></g></symbol>
    <symbol id="i-percent" viewBox="0 0 40 40"><text x="20" y="25" text-anchor="middle" font-family="Oswald, sans-serif" font-weight="700" font-size="14" fill="#fff">100%</text></symbol>
    <symbol id="i-stable" viewBox="0 0 40 40"><g fill="none" stroke="#fff" stroke-width="2.4" stroke-linecap="round" stroke-linejoin="round"><circle cx="20" cy="20" r="14"/><path d="M13 20l5 5 9-10"/></g></symbol>
    <symbol id="i-yield" viewBox="0 0 40 40"><g fill="none" stroke="#fff" stroke-width="2.4" stroke-linecap="round" stroke-linejoin="round"><path d="M20 34V8"/><path d="M11 17l9-9 9 9"/><path d="M8 34h24"/></g></symbol>
  </defs>
</svg>

<main class="dieline">

  <!-- Romanian front with side panel -->
  <section class="carton" lang="ro">
    <article class="face face--ro">
      <div class="ornament" role="img" aria-label="Green hand-drawn flourish frame around the brand name"></div>
      <div class="brand"><span class="brand__dot"></span><span class="brand__name">Don Lucero</span></div>
      <div class="range">Pastry cream</div>
      <div class="hero">
        <h1 class="hero__title">Cremă<br>vegetală<small>pentru cofetării</small></h1>
        <div class="hero__swirl" role="img" aria-label="Illustration of a swirl of whipped cream"></div>
      </div>
      <div class="qty"><span class="qty__label">Cantitate</span><span class="qty__value">℮ 1L</span></div>
      <ul class="uses">
        <li class="use"><div class="use__icon"><svg role="img" aria-label="Whipping"><use href="#i-whip"/></svg></div><p class="use__label">Se bate</p></li>
        <li class="use"><div class="use__icon"><svg role="img" aria-label="Filling"><use href="#i-fill"/></svg></div><p class="use__label">Pentru ganaj</p></li>
        <li class="use"><div class="use__icon"><svg role="img" aria-label="Siphon"><use href="#i-siphon"/></svg></div><p class="use__label">Utilizare cu sifon</p></li>
        <li class="use"><div class="use__icon"><svg role="img" aria-label="100% vegetal fats"><use href="#i-percent"/></svg></div><p class="use__label">100% grăsimi vegetale</p></li>
        <li class="use"><div class="use__icon"><svg role="img" aria-label="High stability"><use href="#i-stable"/></svg></div><p class="use__label">Stabilitate ridicată</p></li>
        <li class="use"><div class="use__icon"><svg role="img" aria-label="High yield"><use href="#i-yield"/></svg></div><p class="use__label">Randament ridicat</p></li>
      </ul>
    </article>

    <aside class="side side--ro">
      <div class="side__block">
        <h2 class="side__heading">Ingrediente</h2>
        <p>Apă, ulei de palmier parţial hidrogenat, zahăr, stabilizatori (E420, E460, E466), emulgatori (E472b, E322 (lecitină din soia), E471), proteine din lapte, sare, aromă, corectori de aciditate (E340, E331), colorant (E160a).</p>
      </div>
      <div class="side__block">
        <h2 class="side__heading">Valori nutriţionale pentru 100g</h2>
        <table class="nutrition">
          <tr><td>Valoare energetică</td><td>290 kcal / 1210 kJ</td></tr>
          <tr><td>Lipide</td><td>28 g</td></tr>
          <tr><td>din care acizi graşi saturaţi</td><td>26 g</td></tr>
          <tr><td>Glucide</td><td>11 g</td></tr>
          <tr><td>din care zaharuri</td><td>9.5 g</td></tr>
          <tr><td>Proteine</td><td>0.6 g</td></tr>
          <tr><td>Sare</td><td>0.05 g</td></tr>
        </table>
      </div>
      <div class="side__block">
        <h2 class="side__heading">Condiții de păstrare</h2>
        <p>Se păstrează la temperaturi între +2°C şi +18°C. A nu se congela. A se consuma înainte de: vezi data pe ambalaj.</p>
      </div>
      <div class="side__block">
        <h2 class="side__heading">Mod de utilizare</h2>
        <p>Pentru a obţine produsul profesional ideal se recomandă ţinerea produsului la frigider, înainte de preparare cu 24 ore (este recomandat ca produsul să aibă o temperatură de maxim 8°C la mixare). Produsul profesional se poate pregăti manual sau cu ajutorul oricărui tip de mixer sau robot de bucătărie. Se recomandă o viteză de mixare medie în prima fază, pentru a evita pierderile prin împrăştiere, după care se poate mixa la viteză mare până la obţinerea consistenţei dorite. Se recomandă să nu se mixeze mai mult decât este necesar. Refrigeraţi produsul mixat.</p>
        <p class="side__highlight">Alegerea profesioniștilor</p>
      </div>
      <div class="maker"><span class="maker__square"></span><span class="maker__name">Valtrum</span></div>
      <p class="origin">Produs în UE</p>
    </aside>
  </section>

  <!-- English front with side panel -->
  <section class="carton">
    <article class="face face--en">
      <div class="ornament" role="img" aria-label="Orange hand-drawn flourish frame around the brand name"></div>
      <div class="brand"><span class="brand__dot"></span><span class="brand__name">Don Lucero</span></div>
      <div class="range">Pastry cream</div>
      <div class="hero">
        <h1 class="hero__title">Vegetable<br>whipping</h1>
        <div class="hero__band"><span>Cream</span></div>
        <div class="hero__swirl" role="img" aria-label="Illustration of a swirl of whipped cream"></div>
      </div>
      <div class="qty"><span class="qty__label">Quantity</span><span class="qty__value">℮ 1L</span></div>
      <ul class="uses">
        <li class="use"><div class="use__icon"><svg role="img" aria-label="Whipping"><use href="#i-whip"/></svg></div><p class="use__label">Whipping</p></li>
        <li class="use"><div class="use__icon"><svg role="img" aria-label="Filling"><use href="#i-fill"/></svg></div><p class="use__label">Filling</p></li>
        <li class="use"><div class="use__icon"><svg role="img" aria-label="Gas whipping"><use href="#i-siphon"/></svg></div><p class="use__label">Gas whipping</p></li>
        <li class="use"><div class="use__icon"><svg role="img" aria-label="100% vegetal fats"><use href="#i-percent"/></svg></div><p class="use__label">100% vegetal fats</p></li>
        <li class="use"><div class="use__icon"><svg role="img" aria-label="High stability"><use href="#i-stable"/></svg></div><p class="use__label">High stability</p></li>
        <li class="use"><div class="use__icon"><svg role="img" aria-label="Best yield in volume"><use href="#i-yield"/></svg></div><p class="use__label">Best yield in volume</p></li>
      </ul>
    </article>

    <aside class="side side--en">
      <div class="side__block">
        <h2 class="side__heading">Ingredients</h2>
        <p>Water, partially hydrogenated palm oil, sugar, stabilizers (E420, E460, E466), emulsifiers (E472b, E322 (soy lecithin), E471), milk protein, salt, flavor, acidity regulators (E340, E331), coloring (E160a).</p>
      </div>
      <div class="side__block">
        <h2 class="side__heading">Nutrition information per 100g</h2>
        <table class="nutrition">
          <tr><td>Energy value</td><td>290 kcal / 1210 kJ</td></tr>
          <tr><td>Fat</td><td>28 g</td></tr>
          <tr><td>of which saturates</td><td>26 g</td></tr>
          <tr><td>Carbohydrate</td><td>11 g</td></tr>
          <tr><td>of which sugars</td><td>9.5 g</td></tr>
          <tr><td>Protein</td><td>0.6 g</td></tr>
          <tr><td>Salt</td><td>0.05 g</td></tr>
        </table>
      </div>
      <div class="side__block">
        <h2 class="side__heading">Storage conditions</h2>
        <p>Store at temperatures between +2°C and +18°C. Do not freeze. Best before: see date on the packaging.</p>
      </div>
      <div class="side__block">
        <h2 class="side__heading">Directions to use</h2>
        <p>To get the ideal output we recommend keeping the product in the refrigerator for 24 hours before using (at mixing the product should have a maximum temperature of 8°C). The professional product can be prepared manually or using any type of mixer or food processor. We recommend a medium mixing speed in the first phase to avoid scattering losses, after which you can mix at high speed until you get the desired consistency. Do not mix more than necessary. Refrigerate mixed product.</p>
        <p class="side__highlight">Professionals' choice</p>
      </div>
      <div class="maker"><span class="maker__square"></span><span class="maker__name">Valtrum</span></div>
      <p class="origin">Produced in EU</p>
    </aside>
  </section>

</main>
</body>
</html>
```